Harbor Scholar Frame

The primary goal would be to develop a new vision for the Harbor Scholar Powerpt. I am attaching an older version called HS, I would like it updated to include our colors and our models with new images that make the presentation more relevant. I am also attaching brochures around the new curriculum. The Links below will give examples to the digital lessons: https://210.quillmora.net/review/content/7c2d4a91-583b-4f7e-b2d6-a4e91c0f5b37/review and https://210.quillmora.net/review/content/9f41b6c3-27da-4e85-81c4-c6d204a8e719/review. the Harbor scholar PWRPT should include some of these images and the color palet from the company brochure which is attached.
Target Market(s)
Education
Look and feel

```html
<!DOCTYPE html>
<html lang="en">
<head>
<meta charset="utf-8">
<title>Harbor Scholar Frame — Slides</title>
<link rel="stylesheet" href="https://fonts.googleapis.com/css2?family=Barlow+Condensed:ital,wght@0,400;0,500;0,600;0,700;0,800;1,700;1,800&family=Roboto+Condensed:wght@400;500&display=swap">
<style>
  :root{
    --canvas:#212122;
    --navy:#1b4f6a;
    --navy-deep:#1d4a61;
    --rule:#2f3a40;
    --ink:#1b1b1b;
    --footer-gray:#5b5b5d;
    --orange:#e8814d;
    --white:#ffffff;
    --cover:#2447a0;
    --cover-dark:#172f74;
  }
  *{box-sizing:border-box;margin:0;padding:0}
  html,body{width:1200px;height:3110px;overflow:hidden}
  body{background:var(--canvas);position:relative;font-family:"Barlow Condensed",sans-serif;color:var(--ink)}

  .slide{position:absolute;left:170px;width:860px;height:645px;background:var(--white);overflow:hidden}
  .slide--evolution{top:137px}
  .slide--platform{top:866px;background:radial-gradient(ellipse at 25% 40%,#ffffff 40%,#eef1f4 100%)}
  .slide--loop{top:1597px}
  .slide--lms{top:2327px}

  .slide__header{position:absolute;left:0;top:0;width:860px;height:73px;background:var(--navy);border-bottom:4px solid var(--rule);
    display:flex;align-items:center;justify-content:center;color:var(--white);font-weight:700;font-size:38px;letter-spacing:.3px}
  .slide__header--caps{font-weight:800;font-size:37px;letter-spacing:1.6px;text-transform:uppercase}

  .slide__art{position:absolute;left:0;top:0;width:860px;height:645px}

  .slide__footer{position:absolute;left:0;bottom:0;width:860px;height:61px}
  .slide__footer svg{position:absolute;left:0;top:0}
  .brand{position:absolute;left:612px;top:0;width:150px;height:61px;display:flex;align-items:center;gap:7px;
    font-family:"Barlow Condensed",sans-serif;font-weight:500;font-size:29px;color:var(--footer-gray)}
  .brand__mark{width:14px;height:14px;background:var(--orange);flex:none}
  .page-no{position:absolute;left:800px;top:0;width:60px;height:61px;display:flex;align-items:center;justify-content:center;
    color:var(--white);font-weight:500;font-size:22px}

  /* slide 2 */
  .excerpt{position:absolute;left:42px;top:122px;width:430px;border-top:2px solid var(--ink);border-bottom:2px solid var(--ink);
    padding:16px 12px 14px 12px;font-family:"Roboto Condensed",sans-serif;font-size:11.4px;line-height:1.42;text-align:justify}
  .excerpt p+p{margin-top:13px}
  .book-cover{position:absolute;left:509px;top:64px;width:321px;height:476px;
    background:linear-gradient(160deg,var(--cover) 0%,var(--cover-dark) 100%);
    box-shadow:10px 12px 20px rgba(0,0,0,.18)}

  /* slide 4 */
  .lms__heading{position:absolute;left:96px;top:184px;font-weight:700;font-size:44px;color:var(--navy)}
  .lms__list{position:absolute;left:96px;top:262px;list-style:none}
  .lms__list li{display:flex;align-items:center;gap:10px;height:43px;font-weight:500;font-size:33px;color:var(--ink)}
  .tick{width:28px;height:28px;flex:none}
</style>
</head>
<body>

<!-- Slide 1 -->
<section class="slide slide--evolution">
  <svg class="slide__art" viewBox="0 0 688 516" width="860" height="645">
    <defs>
      <linearGradient id="photoCool" x1="0" y1="0" x2="1" y2="1"><stop offset="0" stop-color="#4a6f8c"/><stop offset="1" stop-color="#1d2f44"/></linearGradient>
      <linearGradient id="photoWarm" x1="0" y1="0" x2="1" y2="1"><stop offset="0" stop-color="#efe4d2"/><stop offset="1" stop-color="#c8a98a"/></linearGradient>
      <linearGradient id="photoBoard" x1="0" y1="0" x2="1" y2="1"><stop offset="0" stop-color="#e9ecd8"/><stop offset="1" stop-color="#b9a07f"/></linearGradient>
      <linearGradient id="photoScreen" x1="0" y1="0" x2="1" y2="1"><stop offset="0" stop-color="#e6eef4"/><stop offset="1" stop-color="#9fb9cf"/></linearGradient>
      <linearGradient id="photoRoom" x1="0" y1="0" x2="1" y2="1"><stop offset="0" stop-color="#d9d6cf"/><stop offset="1" stop-color="#9c8478"/></linearGradient>
      <radialGradient id="floorShadow"><stop offset="0" stop-color="#000" stop-opacity=".12"/><stop offset="1" stop-color="#000" stop-opacity="0"/></radialGradient>
    </defs>
    <ellipse cx="344" cy="452" rx="230" ry="5" fill="url(#floorShadow)"/>
    <polygon points="190,240 300,240 246,320" fill="#f1ebb6"/>
    <polygon points="380,240 490,240 435,320" fill="#dcecef"/>

    <g stroke="var(--navy-deep)" stroke-width="7">
      <rect role="img" aria-label="Photo: students at computers in a school computer lab" x="86" y="146" width="132" height="132" rx="16" transform="rotate(45 152 212)" fill="url(#photoCool)"/>
      <rect role="img" aria-label="Photo: teacher at an electronic whiteboard" x="180" y="254" width="132" height="132" rx="16" transform="rotate(45 246 320)" fill="url(#photoBoard)"/>
      <rect role="img" aria-label="Photo: pupils working on classroom laptops" x="275" y="146" width="132" height="132" rx="16" transform="rotate(45 341 212)" fill="url(#photoWarm)"/>
      <rect role="img" aria-label="Screenshot: digital lesson screen with progress bars" x="369" y="254" width="132" height="132" rx="16" transform="rotate(45 435 320)" fill="url(#photoScreen)"/>
      <rect role="img" aria-label="Photo: class in front of a projected teaching platform" x="464" y="146" width="132" height="132" rx="16" transform="rotate(45 530 212)" fill="url(#photoRoom)"/>
    </g>

    <g fill="none" stroke="var(--navy-deep)" stroke-width="4" stroke-linecap="round">
      <path d="M114 114 Q100 118 100 134"/><path d="M292 114 Q278 118 278 134"/><path d="M498 114 Q484 118 484 134"/>
      <path d="M330 355 Q330 372 314 374"/><path d="M512 355 Q512 372 496 374"/>
    </g>
    <g fill="var(--navy-deep)">
      <polygon points="94,130 106,130 100,142"/><polygon points="272,130 284,130 278,142"/><polygon points="478,130 490,130 484,142"/>
      <polygon points="324,358 336,358 330,346"/><polygon points="506,358 518,358 512,346"/>
    </g>

    <g font-family="Barlow Condensed, sans-serif" font-size="19" fill="#1b1b1b" font-weight="500">
      <text x="155" y="104" text-anchor="middle">Computer Labs</text>
      <text x="348" y="104" text-anchor="middle">In-class Computing</text>
      <text x="630" y="104" text-anchor="end">Harbor Scholar</text>
      <text x="630" y="127" text-anchor="end">Platforms</text>
      <text x="244" y="432" text-anchor="middle">Electronic Whiteboards</text>
      <text x="468" y="432" text-anchor="middle">Print- Digital</text>
    </g>
    <g font-family="Barlow Condensed, sans-serif" font-size="19" fill="var(--navy)" font-weight="800" font-style="italic">
      <text x="214" y="126" text-anchor="end">1985</text>
      <text x="422" y="126" text-anchor="end">2010</text>
      <text x="630" y="150" text-anchor="end">Next</text>
      <text x="630" y="170" text-anchor="end">Gen</text>
      <text x="314" y="408" text-anchor="middle">2000</text>
      <text x="498" y="408" text-anchor="middle">2012</text>
    </g>
  </svg>
  <header class="slide__header slide__header--caps">Evolution of Digital Instructional Tools</header>
  <footer class="slide__footer">
    <svg width="860" height="61" viewBox="0 0 860 61"><rect width="860" height="61" fill="var(--footer-gray)"/><polygon points="790,0 610,0 590,61 790,61" fill="#fff"/><polygon points="765,0 860,0 860,61 790,61" fill="var(--orange)"/></svg>
    <div class="brand"><span class="brand__mark"></span>Crestline Ed</div>
  </footer>
</section>

<!-- Slide 2 -->
<section class="slide slide--platform">
  <div class="excerpt">
    <p>The Harbor Scholar Platform contains a comprehensive curriculum of guided learning sequences that include applet activities, multimedia presentations, practice exercises, and activities. Before class the teacher uses planning tools to prepare; during class he uses multimedia to introduce a topic, an math tool to explore a mathematics concept, and practice exercises. After class, the teacher can review each student’s progress, trends in the class performance, and begin the process for planning tomorrow’s lessons.</p>
    <p>The platform provides powerful tools to the teacher for planning and managing lessons, customizing instruction to individuals, and providing quick feedback on all activities. It facilitates the management of groups of students without losing focus on individuals. It frees up the teacher for small group work and individual tutoring. In these ways, the platform respects the role of schools in today’s society by teaching to standards and preparing students for high-stakes tests.</p>
    <p>At the same time, the Tidewave Harbor Scholar Platform deploys a social constructivist pedagogy and provides tools and content to build on that approach. It features open-ended explorations, student collaboration, shared work, and group discussion. In this way the platform goes beyond the standards and engages students in their learning, preparing them in a deep way for their place in a technology-rich society.</p>
  </div>
  <div class="book-cover" role="img" aria-label="Photo of the Harbor Scholar Platforms book cover"></div>
  <footer class="slide__footer">
    <svg width="860" height="61" viewBox="0 0 860 61"><rect width="860" height="61" fill="var(--footer-gray)"/><polygon points="790,0 610,0 590,61 790,61" fill="#fff"/><polygon points="765,0 860,0 860,61 790,61" fill="var(--orange)"/></svg>
    <div class="brand"><span class="brand__mark"></span>Crestline Ed</div>
    <div class="page-no">02</div>
  </footer>
</section>

<!-- Slide 3 -->
<section class="slide slide--loop">
  <header class="slide__header">Traditional LMS Instructional Loop</header>
  <svg class="slide__art" viewBox="0 0 688 516" width="860" height="645">
    <g fill="none" stroke-linecap="butt">
      <path d="M140 178 A72 52 0 0 1 289 188" stroke="var(--navy-deep)" stroke-width="19"/>
      <path d="M140 178 A72 52 0 0 1 289 188" stroke="#fff" stroke-width="12"/>
      <path d="M270 314 A72 52 0 0 1 121 304" stroke="var(--navy-deep)" stroke-width="19"/>
      <path d="M270 314 A72 52 0 0 1 121 304" stroke="#fff" stroke-width="12"/>
    </g>
    <polygon points="112,154 164,168 132,184 154,220 96,204" fill="#fff" stroke="var(--navy-deep)" stroke-width="3" stroke-linejoin="round"/>
    <polygon points="299,330 247,316 279,300 257,264 315,280" fill="#fff" stroke="var(--navy-deep)" stroke-width="3" stroke-linejoin="round"/>

    <g fill="var(--navy-deep)">
      <path d="M53 232 H183 Q197 232 197 246 V288 H67 Q53 288 53 274 Z"/>
      <path d="M218 232 H348 Q362 232 362 246 V274 Q362 288 348 288 H218 Z"/>
      <path d="M405 232 H488 V274 Q488 288 474 288 H405 Z"/>
      <path d="M553 232 H636 V274 Q636 288 622 288 H553 Z"/>
      <path d="M365 255 H385 V248 L400 260 L385 272 V265 H365 Z"/>
      <path d="M492 260 L506 248 V255 H536 V248 L550 260 L536 272 V265 H506 V272 Z"/>
    </g>
    <g font-family="Barlow Condensed, sans-serif" font-size="17" font-weight="500" fill="#fff" text-anchor="middle">
      <text x="125" y="257">Content</text><text x="125" y="276">Management</text>
      <text x="290" y="266">Assessment</text>
      <text x="447" y="257">Grade</text><text x="447" y="276">Book</text>
      <text x="594" y="266">SIS</text>
    </g>
  </svg>
  <footer class="slide__footer">
    <svg width="860" height="61" viewBox="0 0 860 61"><rect width="860" height="61" fill="var(--footer-gray)"/><polygon points="790,0 610,0 590,61 790,61" fill="#fff"/><polygon points="765,0 860,0 860,61 790,61" fill="var(--orange)"/></svg>
    <div class="brand"><span class="brand__mark"></span>Crestline Ed</div>
    <div class="page-no">03</div>
  </footer>
</section>

<!-- Slide 4 -->
<section class="slide slide--lms">
  <header class="slide__header">Traditional LMS</header>
  <h2 class="lms__heading">Skinnerian Teaching Machines—ILS’s</h2>
  <ul class="lms__list">
    <li><svg class="tick" viewBox="0 0 28 28"><circle cx="13" cy="15" r="10" fill="none" stroke="var(--navy)" stroke-width="2.4"/><path d="M8 15 L13 20 L25 5" fill="none" stroke="var(--navy)" stroke-width="2.8"/></svg>“Teacher Proof” Technology</li>
    <li><svg class="tick" viewBox="0 0 28 28"><circle cx="13" cy="15" r="10" fill="none" stroke="var(--navy)" stroke-width="2.4"/><path d="M8 15 L13 20 L25 5" fill="none" stroke="var(--navy)" stroke-width="2.8"/></svg>Closed Curriculum</li>
    <li><svg class="tick" viewBox="0 0 28 28"><circle cx="13" cy="15" r="10" fill="none" stroke="var(--navy)" stroke-width="2.4"/><path d="M8 15 L13 20 L25 5" fill="none" stroke="var(--navy)" stroke-width="2.8"/></svg>Fixed Map from Assessment to Curriculum</li>
    <li><svg class="tick" viewBox="0 0 28 28"><circle cx="13" cy="15" r="10" fill="none" stroke="var(--navy)" stroke-width="2.4"/><path d="M8 15 L13 20 L25 5" fill="none" stroke="var(--navy)" stroke-width="2.8"/></svg>Lab or Back of the Room</li>
    <li><svg class="tick" viewBox="0 0 28 28"><circle cx="13" cy="15" r="10" fill="none" stroke="var(--navy)" stroke-width="2.4"/><path d="M8 15 L13 20 L25 5" fill="none" stroke="var(--navy)" stroke-width="2.8"/></svg>One student only</li>
  </ul>
  <footer class="slide__footer">
    <svg width="860" height="61" viewBox="0 0 860 61"><rect width="860" height="61" fill="var(--footer-gray)"/><polygon points="790,0 610,0 590,61 790,61" fill="#fff"/><polygon points="765,0 860,0 860,61 790,61" fill="var(--orange)"/></svg>
    <div class="brand"><span class="brand__mark"></span>Crestline Ed</div>
    <div class="page-no">04</div>
  </footer>
</section>

</body>
</html>
```